Health product web design

I have two websites that look terrible.  They are both 'bee' products related.  The text and links to pages are correct, I just need change the designs.
We are a health product company that sells a range of health and therapeutic products that come from the beehive; including bee pollen, Royal Jelly and Propolis.
The sites to be designed are not ecommerce sites.  They are more information sites that re-direct to our online store (soon to be redesigned) www.corvantaline.com.au
The sites I need revamped are:
www.mellowbrix.com.au
www.tarnivex.com.au
Royal Jelly is a substance made by the worker bees and fed to the Queen Bee.  People take Royal Jelly as it is high in a range of B group vitamins and helps increase energy levels, including sexual stamina.
Propolis is antibacterial, antiviral and has an anesthetic quality.  It is used to put on cuts, burns, sore throats, pimples and mouth & stomach ulcers.  Propolis is collected by bees from the sap of trees and used in the bee hive to sterilise it.
You can read the text (there isnt much) on each site to get an idea of what the products are good for.
The design should be colourful but also communicate credability, trust and a healthy lifestyle with an element of science as the products are sold as health and therapeutic related ie. capsules, liquids, ointments etc.
I am open to questions if you need further information.
Thanks

Target Market(s)
Target market is health supplement buyers 40 - 70 yrs
Industry/Entity Type
Health Product
Requirements
Must have
- Both sites will need a basic logo
Lifestyle images - images of healthy 35ish year old people and/or couples
Nice to have
- Images of bee hives
Close up images of bees, flowers
Images of nature

```html
<!DOCTYPE html>
<html lang="en">
<head>
<meta charset="utf-8">
<title>Royal Jelly – Home</title>
<link rel="stylesheet" href="https://fonts.googleapis.com/css2?family=Arimo:wght@400;700&family=Italianno&family=Oswald:wght@700&display=swap">
<style>
:root{
  --leaf:#7aa51a;
  --leaf-dark:#3f6b06;
  --olive:#8c9550;
  --ink:#4a5418;
  --nav-top:#3a3a3a;
  --nav-bottom:#121212;
  --honey:#e09a1d;
  --honey-dark:#5a3208;
  --frame:#6f8f1c;
  --paper:#ffffff;
  --sky-blue:#2d6e9c;
  --button:#f07d10;
}
*{box-sizing:border-box;margin:0;padding:0}
html,body{width:1091px;height:1200px;overflow:hidden;background:var(--paper)}
body{font-family:"Arimo",Arial,sans-serif}
.page{width:1000px;height:1100px;position:relative;transform:scale(1.091);transform-origin:0 0;overflow:hidden}

.site-header{position:absolute;left:0;top:0;width:1000px;height:95px;background:linear-gradient(#f4fbe9,#e4f3cd)}
.brand{position:absolute;left:92px;top:26px;display:flex;align-items:center;gap:12px}
.brand-square{width:36px;height:36px;background:var(--olive)}
.brand-name{font-size:34px;color:var(--olive);font-weight:400;letter-spacing:1px}
.cert{position:absolute;left:810px;top:10px;width:86px;text-align:center}
.cert-badge{width:56px;height:56px;margin:0 auto;border-radius:50%;border:3px solid var(--leaf);background:#fff}
.cert-caption{font-size:13px;color:var(--leaf);margin-top:6px}

.main-nav{position:absolute;left:0;top:95px;width:1000px;height:50px;background:linear-gradient(var(--nav-top),var(--nav-bottom));display:flex}
.main-nav a{flex:none;color:#e6e6e6;text-decoration:none;font-size:14px;line-height:50px;white-space:nowrap;text-align:center;border-right:1px solid #4a4a4a;box-shadow:1px 0 0 #0a0a0a}
.main-nav a.current{color:#fff}
.main-nav a:last-child{border-right:0;box-shadow:none}
.nav-home{width:74px}
.nav-what{width:168px}
.nav-benefits{width:200px}
.nav-safe{width:164px}
.nav-collected{width:218px}
.nav-buy{width:176px}

.hero{position:absolute;left:0;top:145px;width:1000px;height:250px;background:#fff;border-bottom:3px solid #333}
.hero-photo{position:absolute;left:0;top:0;width:520px;height:247px;background:linear-gradient(90deg,var(--honey-dark) 0%,var(--honey) 45%,#e7a73a 85%,rgba(255,255,255,0) 100%)}
.hero-title{position:absolute;left:550px;top:16px;font-family:"Italianno",cursive;color:var(--olive);font-size:120px;line-height:100px}
.hero-title span{display:block;padding-left:160px}

.sidebar{position:absolute;left:10px;top:412px;width:356px}
.side-block{height:161px}
.side-title{height:27px;background:linear-gradient(#9bc82c,var(--leaf-dark));color:#fff;font-size:16px;line-height:27px;padding-left:8px}
.side-body{position:relative;height:134px}
.side-photo{position:absolute;left:2px;top:8px;width:119px;height:112px;border:3px solid var(--frame);background:radial-gradient(circle at 50% 45%,#f5d35a 0%,#e0ac33 45%,#c9c9c0 80%,#8d7a53 100%)}
.side-text{position:absolute;left:129px;top:10px;width:230px;font-size:13px;line-height:17px;color:var(--ink)}
.side-list{list-style:none}
.side-list li{position:relative;padding-left:20px;margin-bottom:15px}
.side-list svg{position:absolute;left:0;top:3px}
.read-more{position:absolute;right:6px;top:96px;font-size:15px;color:#111;text-decoration:underline}

.divider{position:absolute;left:379px;top:412px;width:1px;height:640px;background:#9a9a9a}

.content{position:absolute;left:396px;top:416px;width:594px;color:var(--ink)}
.content h1{font-size:18px;font-weight:400;color:#2f3a0c;padding-bottom:3px;border-bottom:1px solid #8a8a8a;margin-bottom:8px}
.content p{font-size:14px;line-height:18.6px;margin-bottom:18px}

.promo{position:absolute;left:392px;top:952px;width:600px;height:99px;border:3px solid var(--frame);background:#fff;overflow:hidden;text-decoration:none}
.promo-photo{position:absolute;left:250px;top:0;width:344px;height:93px;background:linear-gradient(90deg,#fff 0%,#f1e2b9 30%,#e3a33a 60%,#b86d14 100%)}
.promo-line1{position:absolute;left:14px;top:4px;font-family:"Oswald",Impact,sans-serif;font-size:23px;line-height:32px;font-weight:700;color:var(--sky-blue);white-space:nowrap}
.promo-line2{position:absolute;left:13px;top:40px;font-family:"Oswald",Impact,sans-serif;font-size:34px;line-height:44px;font-weight:700;color:var(--sky-blue);white-space:nowrap}
.promo-button{position:absolute;left:123px;top:53px;width:97px;height:26px;border-radius:13px;background:linear-gradient(#ffb24a,var(--button));color:#2d5b0d;font-size:15px;font-weight:700;text-align:center;line-height:26px;white-space:nowrap}

.site-footer{position:absolute;left:0;top:1055px;width:1000px;height:45px;background:linear-gradient(#7ca21a,var(--leaf-dark));color:#fff;font-size:11px;text-align:center;line-height:45px}
</style>
</head>
<body>
<div class="page">
  <header class="site-header">
    <div class="brand"><div class="brand-square"></div><div class="brand-name">Royal Jelly</div></div>
    <div class="cert"><div class="cert-badge"></div><div class="cert-caption">Halal Certified</div></div>
  </header>

  <nav class="main-nav">
    <a class="current nav-home" href="#">Home</a>
    <a class="nav-what" href="#">What is Royal Jelly?</a>
    <a class="nav-benefits" href="#">The benefits of Royal Jelly</a>
    <a class="nav-safe" href="#">Is Royal Jelly Safe?</a>
    <a class="nav-collected" href="#">How is Royal Jelly collected?</a>
    <a class="nav-buy" href="#">Buy Royal Jelly online</a>
  </nav>

  <section class="hero">
    <div class="hero-photo" role="img" aria-label="Honey bees working on golden honeycomb"></div>
    <div class="hero-title">Royal<span>Jelly</span></div>
  </section>

  <aside class="sidebar">
    <div class="side-block">
      <div class="side-title">What is Royal Jelly?</div>
      <div class="side-body">
        <div class="side-photo" role="img" aria-label="Bowl of royal jelly with honeycomb"></div>
        <div class="side-text">Strong enough to create a queen bee, Royal Jelly is a nutrition-packed natural substance from which people can also gain strength and vitality.</div>
        <a class="read-more" href="#">Read more...</a>
      </div>
    </div>
    <div class="side-block">
      <div class="side-title">The benefits of Royal Jelly</div>
      <div class="side-body">
        <div class="side-photo" role="img" aria-label="Bowl of royal jelly with honeycomb"></div>
        <ul class="side-text side-list">
          <li><svg width="12" height="10" viewBox="0 0 12 10"><path d="M1 5l3.5 3.5L11 1" fill="none" stroke="#6f9a1a" stroke-width="2.2"/></svg>Assisting in the maintenance of energy, strength and stamina</li>
          <li><svg width="12" height="10" viewBox="0 0 12 10"><path d="M1 5l3.5 3.5L11 1" fill="none" stroke="#6f9a1a" stroke-width="2.2"/></svg>Improving general health and<br>well being</li>
        </ul>
        <a class="read-more" href="#">Read more...</a>
      </div>
    </div>
    <div class="side-block">
      <div class="side-title">Is Royal Jelly Safe?</div>
      <div class="side-body">
        <div class="side-photo" role="img" aria-label="Bowl of royal jelly with honeycomb"></div>
        <div class="side-text">However, Royal Jelly has been reported to cause severe allergic reactions and in rare cases fatalities, especially in asthma and allergy sufferers.</div>
        <a class="read-more" href="#">Read more...</a>
      </div>
    </div>
    <div class="side-block">
      <div class="side-title">How is Royal Jelly collected?</div>
      <div class="side-body">
        <div class="side-photo" role="img" aria-label="Bowl of royal jelly with honeycomb"></div>
        <div class="side-text">Royal Jelly can only be collected from the cell – or honeycomb – of the queen bee larvae. While all bee larvae are fed Royal Jelly in their first few days of</div>
        <a class="read-more" href="#">Read more...</a>
      </div>
    </div>
  </aside>

  <div class="divider"></div>

  <main class="content">
    <h1>Home</h1>
    <p>Royal Jelly is a power pack of nutrition, designed by nature to create the queen bee and used by humans to maintain maximum health. Traditionally recognised for its ability to increase vitality, improve digestion and condition the skin, hair and nails, new benefits of taking Royal Jelly, such as improved liver function, relieving stress, lowering cholesterol, and anti-inflammatory and anti-bacterial properties, are also being discovered.</p>
    <p>Verdane Hive™ Royal Jelly products include fresh Royal Jelly (250gm / 1kg), and Royal Jelly gel capsules (60 / 365 caps). Verdane Hive™ Royal Jelly and Verdane Hive™ Propolis products are selected from the purest beehives – free from chemical or antibiotic sprays.</p>
    <p>You can purchase Verdane Hive™ Royal Jelly from our online store or from one of our trusted suppliers.</p>
    <p>Royal Jelly is a power pack of nutrition, designed by nature to create the queen bee and used by humans to maintain maximum health. Traditionally recognised for its ability to increase vitality, improve digestion and condition the skin, hair and nails, new benefits of taking Royal Jelly, such as improved liver function, relieving stress, lowering cholesterol, and anti-inflammatory and anti-bacterial properties, are also being discovered.</p>
    <p>Verdane Hive™ Royal Jelly products include fresh Royal Jelly (250gm / 1kg), and Royal Jelly gel capsules (60 / 365 caps). Verdane Hive™ Royal Jelly and Verdane Hive™ Propolis products are selected from the purest beehives – free from chemical or antibiotic sprays.</p>
    <p>You can purchase Verdane Hive™ Royal Jelly from our online store or from one of our trusted suppliers.</p>
  </main>

  <a class="promo" href="#">
    <div class="promo-photo" role="img" aria-label="Honey bee beside honeycomb"></div>
    <div class="promo-line1">Buy Royal Jelly</div>
    <div class="promo-line2">Online</div>
    <div class="promo-button">Click Here</div>
  </a>

  <footer class="site-footer">Copyright @ www.mellowbrix.com Allrights reserved</footer>
</div>
</body>
</html>
```